Packaging design coffee brand

Creating a packaging design for coffee products. an existing brand shall be repositioned, complete redesign. capsules, beans, etc. We need a label for the coffee whole bean package, a folded packaging for coffee capsules, see attachment. The package for the whole bean also shall be changed into a full printed packaging.

The logo is already created, but you can play with the elements, the position of symbol and name.

Target Market(s)

Europe

Industry/Entity Type

coffee

Font styles to use
Sans Serif

Requirements
Must have
• we already have a logo, which shall be used. Position of the symbol and name can be adjusted.
Nice to have
• please see the briefing attached, there you find al relevant information.
Should not have
• shall not be ecological, it shal be a lifestyle brand.

```html
<!DOCTYPE html>
<html lang="de">
<head>
<meta charset="utf-8">
<title>Verde Alto – Café Crema Faltschachtel</title>
<link rel="stylesheet" href="https://fonts.googleapis.com/css2?family=Roboto+Slab:wght@400;600;700&family=Allura&family=Montserrat:wght@400&display=swap">
<style>
  :root {
    --page: #e6e7e9;
    --green: #006633;
    --red: #ec1c24;
    --brown: #6b3a06;
    --slate: #7fa3b5;
    --white: #ffffff;
    --ink: #231f20;
    --frame: #333335;
    --grey: #8b8c8e;
  }
  html, body { margin: 0; padding: 0; overflow: hidden; }
  body { width: 1200px; height: 1200px; background: var(--page); position: relative; }
  .dieline { position: absolute; left: 0; top: 0; width: 1200px; height: 1200px; }

  .label {
    position: absolute; left: 488px; top: 565px; width: 224px; height: 267px;
    background: var(--white); box-sizing: border-box; padding: 5px;
  }
  .label__frame {
    width: 100%; height: 100%; box-sizing: border-box;
    border: 5px solid var(--frame); position: relative;
    font-family: "Roboto Slab", serif; color: var(--ink); text-align: center;
  }
  .brand {
    position: absolute; left: 0; right: 0; top: 12px;
    display: flex; flex-direction: column; align-items: center; gap: 4px;
  }
  .brand__dot { width: 11px; height: 11px; border-radius: 50%; background: var(--grey); }
  .brand__name { font-family: "Montserrat", sans-serif; font-size: 10px; letter-spacing: 1px; color: var(--ink); }
  .tag {
    position: absolute; top: 62px; left: 50%; transform: translateX(-50%);
    background: var(--ink); color: var(--white); font-size: 5.5px; padding: 1.5px 3px; white-space: nowrap;
  }
  .title {
    position: absolute; top: 73px; left: 0; right: 0; margin: 0;
    color: var(--green); font-weight: 700; font-size: 14.5px; line-height: 16px;
  }
  .script {
    position: absolute; top: 82px; left: 0; right: 0;
    font-family: "Allura", cursive; color: #c4202a; font-size: 40px; line-height: 40px;
  }
  .claim {
    position: absolute; top: 144px; left: 0; right: 0; margin: 0;
    font-size: 5.6px; line-height: 8px; text-transform: uppercase;
  }
  .variety { position: absolute; top: 176px; left: 0; right: 0; margin: 0; font-size: 11px; font-weight: 600; color: #444; }
  .weight { position: absolute; top: 194px; left: 0; right: 0; font-size: 5.8px; }
  .bean { position: absolute; top: 202px; left: 0; right: 0; font-size: 8px; }
  .sender { position: absolute; top: 221px; left: 0; right: 0; font-size: 4px; line-height: 5.2px; margin: 0; font-style: normal; }
</style>
</head>
<body>
<svg class="dieline" viewBox="0 0 1200 1200" aria-hidden="false">
  <defs>
    <linearGradient id="brushArt" x1="0" y1="0" x2="1" y2="0.3">
      <stop offset="0" stop-color="#006633"/>
      <stop offset="0.25" stop-color="#2f5a33"/>
      <stop offset="0.38" stop-color="#6b3a06"/>
      <stop offset="0.46" stop-color="#7fa3b5"/>
      <stop offset="0.58" stop-color="#ec1c24"/>
      <stop offset="0.72" stop-color="#006633"/>
      <stop offset="0.86" stop-color="#ec1c24"/>
      <stop offset="1" stop-color="#006633"/>
    </linearGradient>
    <linearGradient id="glueZone" x1="0" y1="0" x2="1" y2="0">
      <stop offset="0" stop-color="#f0d6d7"/>
      <stop offset="1" stop-color="#ecdcdd"/>
    </linearGradient>
  </defs>

  <rect x="58" y="118" width="1083" height="806" fill="url(#brushArt)" role="img"
        aria-label="Abstrakte Pinselstrich-Grafik in Grün, Rot, Weiß, Braun und Graublau über alle Seitenflächen"/>

  <rect x="58" y="924" width="1083" height="144" fill="url(#glueZone)" role="img"
        aria-label="Schraffierte Klebe- und Bodenlaschenzone"/>

  <g class="fold-lines" fill="none" stroke="#ec1c24" stroke-width="0.7">
    <polyline points="72,1042 140,1042 245,942 340,1045 437,942 535,1042 668,1042 763,942 860,1045 955,942 1050,1042 1128,1042"/>
  </g>

  <g class="cut-lines" fill="none" stroke="#000" stroke-width="0.8">
    <rect x="58" y="118" width="1083" height="963"/>
    <line x1="82" y1="118" x2="82" y2="1081"/>
    <line x1="245" y1="118" x2="245" y2="1081"/>
    <line x1="437" y1="118" x2="437" y2="1081"/>
    <line x1="763" y1="118" x2="763" y2="1081"/>
    <line x1="955" y1="118" x2="955" y2="1081"/>
    <line x1="1118" y1="118" x2="1118" y2="1081"/>
    <line x1="58" y1="912" x2="1141" y2="912"/>
    <line x1="58" y1="1068" x2="1141" y2="1068"/>
  </g>

  <g class="punch-mark" fill="none" stroke="#000">
    <circle cx="600" cy="433" r="27" stroke-width="1.4" stroke-dasharray="1.5 2"/>
    <circle cx="600" cy="433" r="10" stroke-width="1"/>
  </g>
</svg>

<section class="label">
  <div class="label__frame">
    <div class="brand">
      <span class="brand__dot"></span>
      <span class="brand__name">VERDE ALTO</span>
    </div>
    <span class="tag">100% HANDGEPFLÜCKTER</span>
    <h1 class="title">MEXIKANISCHER<br>JUNGLE GROWN</h1>
    <div class="script">Coffee</div>
    <p class="claim">Pure Lust am Kaffee,<br>so bekömmlich &amp; gar nicht bitter,<br>am besten ohne Zucker</p>
    <h2 class="variety">CAFÉ CREMA</h2>
    <div class="weight">1.000 g</div>
    <div class="bean">Arabica</div>
    <address class="sender">Cafetal Norte<br>Lind &amp; Moreau GbR<br>Hafenweg 14<br>D-20457 Hamburg<br>www.verde-alto-kaffee.de</address>
  </div>
</section>
</body>
</html>
```